Business Card Design

We need a design that will also transfer to car decals
We need a design that will speak to the average person needing home and office remodeling
The design should be fresh, exciting, easy to read in a glance and unique
We would like a die-cut tool belt
Bright colors and evenly spaced information

Target Market(s)

Home and business owners
Middle and Upper Income property owners
Families and people with fixer upper homes

Industry/Entity Type

Business

Contact Information for Business Card

Looking for the best Bay Area Handyman? Here I am!
RKW Handyman Services does it all at prices regular people can afford.
Electrical, Plumbing, Carpentry, Remodeling, Fencing, Picture and window placement, Hauling ... and anything else you can imagine!
510-473-2918
Serving the Entire Bay Area
Free Estimates! Call us Today to turn your dreams into reality!

Font styles to use
Serif

Requirements
Must have
• Speaks to the average person
stands out among similar industry cards
Nice to have
• fun, comical, you want to hold on to this card
Should not have
• bland colors
look too crowded

```html
<!DOCTYPE html>
<html lang="en">
<head>
<meta charset="utf-8">
<title>RKW Handyman Services – Business Card</title>
<link rel="stylesheet" href="https://fonts.googleapis.com/css2?family=Noto+Sans:wght@400;700&display=swap">
<style>
  :root {
    --backdrop: #e9e6e2;
    --card-light: #ffffff;
    --card-edge: #d9dadb;
    --ink: #2f3b45;
    --ink-dark: #333333;
    --brand-blue: #0a7cc7;
    --brand-blue-light: #3aa6e6;
    --rule-grey: #b8bcc0;
  }
  * { box-sizing: border-box; margin: 0; padding: 0; }
  html, body {
    width: 1200px;
    height: 900px;
    overflow: hidden;
    background: var(--backdrop);
    font-family: "Noto Sans", "DejaVu Sans", sans-serif;
    color: var(--ink);
  }
  .canvas {
    position: relative;
    width: 1200px;
    height: 900px;
  }
  .card {
    position: absolute;
    left: 308px;
    width: 565px;
    height: 312px;
    background: radial-gradient(ellipse at 50% 40%, var(--card-light) 0%, #f1f2f3 60%, var(--card-edge) 100%);
    border: 1px solid #9a9a9a;
    box-shadow: 3px 4px 6px rgba(0,0,0,0.25);
    overflow: hidden;
  }
  .card-front { top: 84px; }
  .card-back { top: 475px; }

  /* Front */
  .brand {
    position: absolute;
    left: 82px;
    top: 0;
    height: 100%;
    display: flex;
    align-items: center;
    gap: 16px;
  }
  .brand-square {
    width: 120px;
    height: 120px;
    background: linear-gradient(160deg, var(--brand-blue-light), var(--brand-blue));
  }
  .brand-name {
    font-size: 40px;
    font-weight: 700;
    color: var(--ink-dark);
    letter-spacing: -0.5px;
  }

  /* Back */
  .headline {
    position: absolute;
    top: 20px;
    width: 100%;
    text-align: center;
    font-size: 20px;
  }
  .wave {
    position: absolute;
    left: 0;
    top: 58px;
    width: 565px;
    height: 60px;
  }
  .greeting {
    position: absolute;
    left: 38px;
    top: 94px;
    font-size: 23px;
  }
  .services {
    position: absolute;
    top: 144px;
    width: 100%;
    padding: 0 28px;
    text-align: center;
    font-size: 13.6px;
    line-height: 1.32;
  }
  .invite {
    position: absolute;
    top: 212px;
    width: 100%;
    text-align: center;
    font-size: 13.6px;
    line-height: 1.32;
  }
  .phone {
    position: absolute;
    top: 252px;
    width: 100%;
    text-align: center;
    font-size: 40px;
    letter-spacing: 0.5px;
  }
</style>
</head>
<body>
<main class="canvas">
  <section class="card card-front" aria-label="Card front">
    <div class="brand">
      <div class="brand-square"></div>
      <span class="brand-name">RKW Handyman</span>
    </div>
  </section>

  <section class="card card-back" aria-label="Card back">
    <p class="headline">Looking for the best Bay Area Handyman?</p>
    <svg class="wave" viewBox="0 0 565 60" preserveAspectRatio="none" aria-hidden="true">
      <path d="M0 14 C120 4 260 10 370 26 C450 36 520 20 565 6 L565 56 C500 60 440 56 370 48 C260 30 120 18 0 18 Z" fill="var(--brand-blue)"/>
      <path d="M0 14 C120 4 260 10 370 26 C450 36 520 20 565 6" fill="none" stroke="var(--rule-grey)" stroke-width="1.5"/>
    </svg>
    <p class="greeting">Here I am!</p>
    <p class="services">RKW Handyman Services does it all at prices regular people can afford. Electrical, Plumbing, Carpentry, Remodeling, Fencing, Picture and window placement, Hauling ... And anything else you can imagine!</p>
    <p class="invite">Serving the Entire Bay Area Free Estimates!<br>Call us Today to turn your dreams into reality!</p>
    <p class="phone">510-473-2918</p>
  </section>
</main>
</body>
</html>
```